Easter & Summer School Dance Camps

I need two flyers one for Easter camps and one for summer school
We are a performing arts and dance academy

I want a double sided flyers one side summer school one side easter camp
Updates

Please make these flyers appeal to young dancers and performers - eye catching up to date Added Tuesday, March 1, 2016

Target Market(s)

Young children and teenagers

Industry/Entity Type

School

Font styles to use
Serif
Sans Serif

Requirements
Must have
• bright colourful

```html
<!DOCTYPE html>
<html lang="en">
<head>
<meta charset="utf-8">
<title>Brightstep Easter Workshops Flyer</title>
<link rel="stylesheet" href="https://fonts.googleapis.com/css2?family=Smokum&family=Questrial&family=Kaushan+Script&family=Oswald:wght@300;400;600&display=swap">
<style>
  :root {
    --page: #ffffff;
    --mist: #e9e9ea;
    --frame: #2a2a2a;
    --title-blue: #3a4a9a;
    --title-shadow: #b9bccb;
    --pink: #e0308a;
    --body-grey: #6d6d6d;
    --orange: #f28a2e;
    --ink: #3a3a3a;
    --faint: rgba(255,255,255,0.85);
  }
  * { box-sizing: border-box; margin: 0; padding: 0; }
  html, body { width: 849px; height: 1200px; overflow: hidden; background: var(--page); }
  .flyer {
    position: relative;
    width: 849px;
    height: 1200px;
    background: var(--page);
    overflow: hidden;
  }
  .flyer__frame {
    position: absolute;
    left: 21px; top: 22px; width: 807px; height: 1156px;
    border: 1px solid var(--frame);
    background:
      radial-gradient(ellipse at 65% 30%, #ffffff 0%, rgba(255,255,255,0) 55%),
      linear-gradient(180deg, var(--mist) 0%, #f6f6f6 30%, #ffffff 45%, #ffffff 68%, #f0f0f0 82%, #d9d9d9 100%);
    overflow: hidden;
  }
  .hero-art {
    position: absolute;
    left: 405px; top: 0; width: 330px; height: 420px;
    background:
      radial-gradient(ellipse at 48% 30%, rgba(60,40,30,0.85) 0%, rgba(190,80,30,0.7) 22%, rgba(240,170,40,0.45) 42%, rgba(255,255,255,0) 68%);
  }
  .title {
    position: absolute;
    left: 52px; top: 60px;
    font-family: "Smokum", serif;
    font-size: 92px;
    line-height: 94px;
    color: var(--title-blue);
    text-shadow: 5px 5px 0 var(--title-shadow);
    letter-spacing: 1px;
  }
  .intro {
    position: absolute;
    left: 52px; top: 378px; width: 700px;
    font-family: "Questrial", sans-serif;
    color: var(--body-grey);
    font-size: 18.5px;
    line-height: 24px;
  }
  .intro__heading {
    color: var(--pink);
    font-size: 19px;
    margin-bottom: 2px;
  }
  .intro p { margin-bottom: 24px; }
  .workshop-title {
    position: absolute;
    left: 44px; top: 700px;
    font-family: "Kaushan Script", cursive;
    color: var(--orange);
    font-size: 88px;
    line-height: 110px;
    white-space: nowrap;
  }
  .brand-echo {
    position: absolute;
    left: 690px; top: 1140px;
    transform: rotate(-90deg);
    transform-origin: left top;
    font-family: "Oswald", sans-serif;
    font-weight: 300;
    font-size: 110px;
    color: var(--faint);
    white-space: nowrap;
    line-height: 1;
  }
  .details {
    position: absolute;
    left: 429px; top: 838px; width: 330px;
    font-family: "Oswald", sans-serif;
    color: var(--ink);
  }
  .details__lead {
    font-weight: 600;
    font-size: 18.5px;
    line-height: 27px;
    margin-bottom: 30px;
  }
  .details__info {
    font-weight: 300;
    font-size: 12.5px;
    line-height: 17px;
  }
  .details__info p { margin-bottom: 17px; }
  .brand {
    position: absolute;
    left: 40px; top: 955px;
    display: flex; align-items: center; gap: 12px;
    font-family: "Questrial", sans-serif;
    color: #111111;
  }
  .brand__dot { width: 22px; height: 22px; border-radius: 50%; background: var(--pink); }
  .brand__name { font-size: 64px; line-height: 1; }
  .brand__tag {
    position: absolute;
    left: 40px; top: 1040px; width: 310px;
    font-family: "Questrial", sans-serif;
    font-size: 9px;
    letter-spacing: 0.3px;
    color: #111111;
  }
</style>
</head>
<body>
  <main class="flyer">
    <div class="flyer__frame">
      <div class="hero-art" role="img" aria-label="Dynamic illustration of a leaping dancer bursting into orange and gold paint splashes"></div>

      <h1 class="title">Once<br>Upon a<br>Time...</h1>

      <section class="intro">
        <h2 class="intro__heading">EASTER WORKSHOPS</h2>
        <p>This spring, your child will enjoy a joyous journey to the magical<br>world of Once Upon a Time for a fabulous springtime treat.</p>
        <p>We will work our magic to ensure your child enjoys every minute.<br>Guiding each child every step of the way and inspire and encourage<br>them to project their voices, learn energetic dance routines,<br>&nbsp;catchy songs, and more importantly HAVE FUN!</p>
        <p>Tuesday 5 &amp; 6 April 2016<br>Age 3 – 7 years<br>10 – 12pm 18 per day<br>or 30 for both days</p>
      </section>

      <h2 class="workshop-title">West end workshop.</h2>

      <div class="brand-echo" aria-hidden="true">brightstep</div>

      <section class="details">
        <p class="details__lead">Our Easter dance camps are fun,<br>fresh and funky, mixed together<br>with a little musical theatre!</p>
        <div class="details__info">
          <p>WEST END WORKSHOP<br>Tuesday 5 &amp; 6 April 2016<br>8 – 16 years<br>1-4pm</p>
          <p>30 per day/ 55 for both</p>
          <p>Venue The Parish Hall of St Anselm Elmbridge Green KT9 0ZZ</p>
          <p>Email brightstepdance@mail.com to book or text 07700900123</p>
        </div>
      </section>

      <div class="brand">
        <span class="brand__dot"></span>
        <span class="brand__name">brightstep</span>
      </div>
      <p class="brand__tag">ACADEMY OF DANCE AND PERFORMING ARTS</p>
    </div>
  </main>
</body>
</html>
```